we need a homepage for a marketplace

We manage all projects using our ground-breaking platform Velbrim Portal. You get access to 150+ partners in 70 countries, security, cost efficiency, technical skills, speed, 100% visibility and accountability.Velbrim aims to help clients realize the full potential of their investments, provide a competitive price, establish the business need as a competitive advantage, and provide a strategic business asset that can facilitate growth.
Target Market(s)
Freelancers
Industry/Entity Type
Business Software
Number of Pages Required
1 page
Requirements
Must have
- Credentials -http://qlvtk.com/freelancer/public
- Front :
- Client:
- Email id - doriek@fallowquartzsystems.com
- Password - 123456
- Partner:
- Email id - mortenl@fallowquartzsystems.com
- Password - 123456
- Project Manager:
- Email id - lorcan@fallowquartzsystems.com
- Password - 123456
Nice to have
- It will be nice to have a creative design, and a outside the box look/feel

```html
<!DOCTYPE html>
<html lang="en">
<head>
<meta charset="utf-8">
<title>Velbrim Dashboard</title>
<link href="https://fonts.googleapis.com/css2?family=Questrial&family=Poppins:wght@100;400;600;700&display=swap" rel="stylesheet">
<style>
:root{
  --navy:#2c3a5e;
  --card:#33456e;
  --side:#333333;
  --foot:#232323;
  --blue:#1a5cff;
  --white:#ffffff;
  --muted:#8a8f99;
  --line:rgba(255,255,255,.35);
  --plus:#8d96ab;
}
*{margin:0;padding:0;box-sizing:border-box}
html,body{width:1200px;height:1040px;overflow:hidden;background:var(--navy);font-family:'Questrial',sans-serif;color:var(--white)}
.page{position:relative;width:1200px;height:1040px}
.brand{position:absolute;left:0;top:0;width:160px;height:80px;background:var(--white);display:flex;align-items:center;justify-content:center;color:#2c3a5e;font-size:24px}
.topbar{position:absolute;left:160px;top:0;width:1040px;height:80px;border-bottom:1px solid rgba(255,255,255,.06)}
.nav a{position:absolute;top:32px;font-size:13px;letter-spacing:.5px;color:var(--white);text-decoration:none;transform:translateX(-50%)}
.nav .active-bar{position:absolute;left:64px;top:77px;width:147px;height:3px;background:var(--blue)}
.pill{position:absolute;border:1px solid var(--line);border-radius:16px;display:flex;align-items:center;justify-content:center;font-family:'Poppins',sans-serif;font-weight:600;font-size:12.5px;gap:8px}
.sidebar{position:absolute;left:0;top:80px;width:160px;height:833px;background:var(--side)}
.avatar{position:absolute;left:42px;top:18px;width:76px;height:76px;border-radius:50%;border:3px solid #555;background:radial-gradient(circle at 50% 40%,#b48d74,#6f6a6c)}
.round-icon{position:absolute;top:44px;width:28px;height:28px;border-radius:50%;border:2px solid #555;display:flex;align-items:center;justify-content:center}
.user-name{position:absolute;top:106px;width:160px;text-align:center;font-size:18px}
.user-role{position:absolute;left:23px;top:128px;font-family:'Poppins',sans-serif;font-weight:700;font-size:9px;color:var(--blue)}
.edit-btn{position:absolute;left:25px;top:159px;width:113px;height:29px;border:1px solid #555;border-radius:15px;font-size:10px;color:#666;display:flex;align-items:center;justify-content:center}
.menu-item{position:absolute;left:0;width:160px;display:flex;align-items:center;font-family:'Poppins',sans-serif;font-size:10.5px}
.menu-item svg{margin-left:13px;margin-right:10px}
.menu-item .chev{position:absolute;right:5px}
.toggle{position:absolute;left:28px;top:510px;width:106px;height:27px;border:1px solid #4a4a4a;border-radius:14px}
.toggle .on{position:absolute;left:3px;top:3px;width:21px;height:21px;border-radius:50%;background:var(--blue);font-family:'Poppins',sans-serif;font-size:8px;font-weight:700;color:#15213f;display:flex;align-items:center;justify-content:center}
.toggle .off{position:absolute;right:8px;top:7px;font-size:8px;color:#666;font-family:'Poppins',sans-serif}
.title{position:absolute;left:199px;top:124px;font-size:19.5px;letter-spacing:.5px}
.card{position:absolute;width:320px;height:320px;background:var(--card)}
.card .num{position:absolute;left:20px;top:2px;font-family:'Poppins',sans-serif;font-weight:100;font-size:158px;line-height:1;color:var(--blue);letter-spacing:-12px}
.card .label{position:absolute;left:134px;top:131px;font-size:16px;letter-spacing:-.6px}
.card .btn{position:absolute;left:82px;top:218px;width:156px;height:29px;border:1px solid var(--line);border-radius:15px;font-size:16px;display:flex;align-items:center;justify-content:center}
.add-card{position:absolute;left:533px;top:519px;width:320px;height:320px;border:1px dashed #4b64a8}
.add-card .btn{position:absolute;left:67px;top:217px;width:184px;height:29px;border:1px solid var(--line);border-radius:15px;font-size:16px;display:flex;align-items:center;justify-content:center}
.footer{position:absolute;left:0;top:913px;width:1200px;height:127px;background:var(--foot);font-size:15px}
.footer span{position:absolute;top:54px}
.footer b{font-family:'Poppins',sans-serif;font-weight:700;font-size:14px}
.footer .sq{position:absolute;top:62px;width:7px;height:7px;background:var(--blue)}
</style>
</head>
<body>
<div class="page">
  <div class="brand">Velbrim</div>

  <header class="topbar">
    <nav class="nav">
      <a href="#" style="left:134px">HOME</a>
      <a href="#" style="left:290px">ABOUT US</a>
      <a href="#" style="left:472px">CONTACT US</a>
      <div class="active-bar"></div>
    </nav>
    <div class="pill" style="left:793px;top:26px;width:106px;height:28px">ACCOUNT
      <svg width="14" height="8" viewBox="0 0 14 8"><path d="M1 2 Q7 8 13 1" stroke="#1a5cff" stroke-width="2.5" fill="none"/></svg>
    </div>
    <div class="pill" style="left:937px;top:26px;width:70px;height:28px">LOGOUT</div>
  </header>

  <aside class="sidebar">
    <div class="round-icon" style="left:8px">
      <svg width="13" height="9" viewBox="0 0 13 9"><rect x=".5" y=".5" width="12" height="8" fill="#ddd"/><path d="M.5 .5 6.5 5 12.5 .5" stroke="#555" fill="none"/></svg>
    </div>
    <div class="avatar" role="img" aria-label="Profile photo of the user"></div>
    <div class="round-icon" style="left:128px">
      <svg width="13" height="13" viewBox="0 0 24 24"><path d="M6 2l4 5-2 3c1 3 3 5 6 6l3-2 5 4-3 4C10 21 3 14 2 5z" fill="#ddd"/></svg>
    </div>
    <div class="user-name">Aldric Venn</div>
    <div class="user-role">Lead Technician</div>
    <div class="edit-btn">Edit Profile</div>

    <div class="menu-item" style="top:234px">
      <svg width="17" height="15" viewBox="0 0 17 15"><rect x="1" y="10" width="2" height="5" fill="#fff"/><rect x="5" y="8" width="2" height="7" fill="#fff"/><rect x="9" y="5" width="2" height="10" fill="#fff"/><rect x="13" y="2" width="2" height="13" fill="#fff"/><path d="M1 8 6 4 9 6 15 1" stroke="#fff" fill="none"/></svg>
      Dashboard
      <svg class="chev" width="8" height="12" viewBox="0 0 8 12"><path d="M1 1 6 6 1 11" stroke="#1a5cff" stroke-width="2.5" fill="none"/></svg>
    </div>
    <div class="menu-item" style="top:289px">
      <svg width="14" height="18" viewBox="0 0 14 18"><path d="M0 0h9l5 5v13H0z" fill="#fff"/><path d="M7 14V7M4 10l3-3 3 3" stroke="#333" stroke-width="1.6" fill="none"/></svg>
      Open Projects
    </div>
    <div class="menu-item" style="top:344px">
      <svg width="14" height="18" viewBox="0 0 14 18"><path d="M0 0h9l5 5v13H0z" fill="#fff"/><path d="M7 7v7M3.5 10.5h7" stroke="#333" stroke-width="2"/></svg>
      Working Projects
    </div>
    <div class="menu-item" style="top:400px">
      <svg width="14" height="18" viewBox="0 0 14 18"><path d="M0 0h9l5 5v13H0z" fill="#fff"/><path d="M3 10l3 3 5-6" stroke="#333" stroke-width="1.8" fill="none"/></svg>
      Completed Projects
    </div>
    <div class="menu-item" style="top:455px">
      <svg width="17" height="15" viewBox="0 0 17 15"><path d="M6 2h11M6 7.5h11M6 13h11" stroke="#fff" stroke-width="1.5"/><path d="M0 2l1.5 1.5L4 0.5M0 7.5l1.5 1.5L4 6M0 13l1.5 1.5L4 11.5" stroke="#fff" fill="none"/></svg>
      Transactions
    </div>

    <div class="toggle">
      <div class="on">ON</div>
      <svg style="position:absolute;left:44px;top:4px" width="18" height="18" viewBox="0 0 18 18"><path d="M9 2c-3 0-5 2-5 5v4l-2 2h14l-2-2V7c0-3-2-5-5-5z" fill="#888"/><circle cx="9" cy="15.5" r="1.8" fill="#888"/></svg>
      <div class="off">OFF</div>
    </div>
  </aside>

  <h1 class="title">THE VELBRIM DASHBOARD</h1>

  <section class="card" style="left:199px;top:183px">
    <div class="num">13</div><div class="label">OPEN PROJECTS</div><div class="btn">View Details</div>
  </section>
  <section class="card" style="left:533px;top:183px">
    <div class="num">7</div><div class="label">WORKING PROJECTS</div><div class="btn">View Details</div>
  </section>
  <section class="card" style="left:866px;top:183px">
    <div class="num">2</div><div class="label">COMPLETED PROJECTS</div><div class="btn">View Details</div>
  </section>
  <section class="card" style="left:199px;top:519px">
    <div class="num">4</div><div class="label">CANCELED PROJECTS</div><div class="btn">View Details</div>
  </section>
  <section class="add-card">
    <svg style="position:absolute;left:100px;top:80px" width="120" height="120" viewBox="0 0 120 120"><path d="M60 0v120M0 60h120" stroke="var(--plus)" stroke-width="6"/></svg>
    <div class="btn">ADD PROJECT LINK</div>
  </section>

  <footer class="footer">
    <span style="left:82px">Copyright 2016 <b>THE VELBRIM</b>. ALL Rights Reserved.</span>
    <span style="left:666px">Privacy Policy</span>
    <i class="sq" style="left:793px"></i>
    <span style="left:838px">Terms &amp; Conditions</span>
    <i class="sq" style="left:1009px"></i>
    <span style="left:1040px">Sitemap</span>
  </footer>
</div>
</body>
</html>
```